Support People to improve their image and well-being by provided personalised advise

We need a design for business cards that could be used for production on brightleaf press. We build a new business in our region for advising mostly women (also men though) on style embracing several aspects including fashion, style, self-confidence and ultimately your internal and external image. The business card should be "classy", "french-style". The business is located in the french -speaking part of Switzerland, close to France. The name of the company is Lunor Mode

Target Market(s)

Service fees won't be cheap (medium to premium) thus we target mid-class to upper-class women (1st target) and men (2nd target)

Industry/Entity Type

Life Coaching

Contact Information for Business Card

Conseil en Image

+41 78 514 62 07
selmaroux@lunor-mode.example
linkedin.com/in/roux-dal-selma

Logo Text

Lunor Mode

Colors

Designer to choose colors to be used in the design.

```html
<!DOCTYPE html>
<html lang="fr">
<head>
<meta charset="utf-8">
<title>Lunor Mode – Cartes de visite</title>
<link rel="stylesheet" href="https://fonts.googleapis.com/css2?family=Fira+Sans+Condensed:wght@600;700&display=swap">
<style>
  :root {
    --bg: #ece9e4;
    --ink: #1d1d1d;
    --gold: #b49a52;
    --cream: #efebe6;
    --hatch: #d9d4ce;
    --rule: #4a4a4a;
  }
  * { margin: 0; padding: 0; box-sizing: border-box; }
  html, body { width: 1200px; height: 800px; overflow: hidden; background: var(--bg); }
  body { position: relative; font-family: "Fira Sans Condensed", "Arial Narrow", sans-serif; }

  .card {
    position: absolute;
    top: 245px;
    width: 540px;
    height: 309px;
    overflow: hidden;
    box-shadow: 0 8px 24px rgba(0,0,0,.12);
  }
  .card--front { left: 40px; background: var(--ink); }
  .card--back { left: 620px; background: var(--cream); }

  .card__accents { position: absolute; inset: 0; }

  .brand {
    position: absolute;
    display: flex;
    flex-direction: column;
    align-items: center;
    color: var(--gold);
  }
  .brand__dot {
    width: 58px; height: 58px;
    border: 2px solid var(--gold);
    border-radius: 50%;
    margin-bottom: 8px;
  }
  .brand__name {
    font-weight: 700;
    font-size: 40px;
    line-height: 1;
    letter-spacing: .5px;
    text-transform: uppercase;
  }
  .brand__tagline {
    font-weight: 700;
    font-size: 13px;
    letter-spacing: .3px;
    text-transform: uppercase;
    margin-top: 3px;
  }
  .card--front .brand { left: 0; right: 0; top: 92px; }
  .card--front .brand__dot { width: 74px; height: 74px; }
  .card--front .brand__name { font-size: 48px; }
  .card--front .brand__tagline { font-size: 15px; }

  .card--back .brand { left: 30px; width: 230px; top: 84px; }
  .card--back .brand__name { font-size: 34px; }

  .edge-band {
    position: absolute;
    background: var(--hatch);
  }
  .edge-band--top { left: 0; right: 0; top: 0; height: 10px; }
  .edge-band--bottom { left: 0; right: 0; bottom: 0; height: 10px; }
  .edge-band--left { top: 0; bottom: 0; left: 0; width: 10px; }
  .edge-band--right { top: 0; bottom: 0; right: 0; width: 10px; }

  .divider {
    position: absolute;
    left: 282px;
    top: 48px;
    height: 212px;
    width: 1px;
    background: var(--rule);
  }

  .contact {
    position: absolute;
    left: 306px;
    top: 122px;
    list-style: none;
    color: var(--gold);
    font-weight: 600;
    font-size: 14px;
    line-height: 1.45;
  }
</style>
</head>
<body>

  <section class="card card--front" aria-label="Recto">
    <svg class="card__accents" viewBox="0 0 540 309" aria-hidden="true">
      <g stroke="#b49a52" stroke-width="2">
        <line x1="360" y1="0" x2="455" y2="140"/>
        <line x1="385" y1="0" x2="480" y2="140"/>
        <line x1="60" y1="170" x2="150" y2="309"/>
        <line x1="85" y1="170" x2="175" y2="309"/>
      </g>
    </svg>
    <div class="brand">
      <span class="brand__dot"></span>
      <span class="brand__name">Lunor Mode</span>
      <span class="brand__tagline">Conseil en image</span>
    </div>
  </section>

  <section class="card card--back" aria-label="Verso">
    <div class="edge-band edge-band--top" role="img" aria-label="Bordure hachurée fine"></div>
    <div class="edge-band edge-band--bottom" role="img" aria-label="Bordure hachurée fine"></div>
    <div class="edge-band edge-band--left" role="img" aria-label="Bordure hachurée fine"></div>
    <div class="edge-band edge-band--right" role="img" aria-label="Bordure hachurée fine"></div>

    <div class="brand">
      <span class="brand__dot"></span>
      <span class="brand__name">Lunor Mode</span>
      <span class="brand__tagline">Conseil en image</span>
    </div>

    <div class="divider"></div>

    <ul class="contact">
      <li>+41 78 514 62 07</li>
      <li>selmaroux@lunor-mode.example</li>
      <li>linkedin.com/in/roux-dal-selma</li>
    </ul>
  </section>

</body>
</html>
```